We are needing a bookcover for a reprint of our book "Whispers Beneath the Amber Horizon". It takes a look at the geologic formation found in the great plains. Our original cover was colorful and showed rock layers. Something similar but different and eye catching would be great. a geologic cross section showing various layers or possibly some different rocks/soils. We are really open to suggestions attached is the current book cover with the colored layers and the cover from the 80s.

Target Market(s)

Adult Readers

Industry/Entity Type

Nonprofit retail - science - nature

Requirements
Must have
• Geology or rock layers
Nice to have
• Books title, Geologic cross section
Should not have
• People or animals, no photos prefer sketch

```html
<!DOCTYPE html>
<html lang="en">
<head>
<meta charset="utf-8">
<title>Whispers Beneath the Amber Horizon — Book Cover</title>
<link rel="stylesheet" href="https://fonts.googleapis.com/css2?family=Oswald:wght@500;600&display=swap">
<style>
  :root {
    --backdrop: #e9e9e9;
    --cover-paper: #ffffff;
    --cover-texture: #f4f5f4;
    --ink: #141414;
    --strata-pale: #eef5f1;
    --strata-mint: #a9d9c2;
    --strata-green: #3f8f6c;
    --strata-moss: #5f9f7f;
    --strata-deep: #1f3b2e;
    --strata-stone: #c9d6cf;
    --shadow: rgba(0, 0, 0, 0.35);
  }
  * { margin: 0; padding: 0; box-sizing: border-box; }
  html, body {
    width: 1020px;
    height: 1200px;
    overflow: hidden;
    background: var(--backdrop);
  }
  .book-cover {
    position: absolute;
    left: 120px;
    top: 15px;
    width: 780px;
    height: 1170px;
    background: linear-gradient(180deg, var(--cover-paper) 0%, var(--cover-texture) 55%, var(--cover-paper) 100%);
    overflow: hidden;
  }
  .cover-title {
    position: absolute;
    top: 51px;
    left: 0;
    width: 100%;
    text-align: center;
    font-family: "Oswald", "Arial Narrow", sans-serif;
    font-weight: 600;
    color: var(--ink);
    letter-spacing: -1px;
    font-size: 100px;
    line-height: 136px;
  }
  .cover-title .line { display: block; white-space: nowrap; }
  .cover-title .line-small { font-size: 50px; }
  .cover-title .line-wide { font-size: 98px; }
  .cover-art {
    position: absolute;
    left: 71px;
    top: 477px;
    width: 636px;
    height: 540px;
    box-shadow: 6px 8px 8px var(--shadow);
  }
  .cover-art svg { display: block; width: 100%; height: 100%; }
</style>
</head>
<body>
  <main class="book-cover">
    <h1 class="cover-title">
      <span class="line">WHISPERS</span>
      <span class="line">Beneath <span class="line-small">the</span></span>
      <span class="line line-wide">AMBER HORIZON</span>
    </h1>
    <figure class="cover-art">
      <svg role="img" aria-label="Sketched illustration of a layered canyon: horizontal rock strata with waterfalls spilling over the ledges into a pool, in green and black ink" viewBox="0 0 636 540" preserveAspectRatio="none">
        <rect class="stratum" x="0" y="0" width="636" height="40" fill="var(--strata-pale)"/>
        <rect class="stratum" x="0" y="40" width="636" height="22" fill="var(--strata-moss)"/>
        <rect class="stratum" x="0" y="62" width="636" height="34" fill="var(--strata-stone)"/>
        <rect class="stratum" x="0" y="96" width="636" height="48" fill="var(--strata-green)"/>
        <rect class="stratum" x="0" y="144" width="636" height="30" fill="var(--strata-mint)"/>
        <rect class="stratum" x="0" y="174" width="636" height="44" fill="var(--strata-moss)"/>
        <rect class="stratum" x="0" y="218" width="636" height="26" fill="var(--strata-deep)"/>
        <rect class="stratum" x="0" y="244" width="636" height="60" fill="var(--strata-pale)"/>
        <rect class="stratum" x="0" y="304" width="636" height="40" fill="var(--strata-mint)"/>
        <rect class="stratum" x="0" y="344" width="636" height="50" fill="var(--strata-stone)"/>
        <rect class="stratum" x="0" y="394" width="636" height="36" fill="var(--strata-green)"/>
        <rect class="stratum" x="0" y="430" width="636" height="50" fill="var(--strata-mint)"/>
        <rect class="stratum" x="0" y="480" width="636" height="60" fill="var(--strata-deep)"/>
        <g stroke="var(--ink)" stroke-width="1.5" opacity="0.5">
          <line x1="0" y1="40" x2="636" y2="40"/>
          <line x1="0" y1="96" x2="636" y2="96"/>
          <line x1="0" y1="174" x2="636" y2="174"/>
          <line x1="0" y1="244" x2="636" y2="244"/>
          <line x1="0" y1="344" x2="636" y2="344"/>
          <line x1="0" y1="430" x2="636" y2="430"/>
          <line x1="0" y1="480" x2="636" y2="480"/>
        </g>
      </svg>
    </figure>
  </main>
</body>
</html>
```